Flyer-Design für Karin Dossow
Zielgruppe
Ich bin psychologische Beraterin und Heilpraktikerin für Psychotherapie. Ich biete ein Coaching speziell für Mütter (meist Mütter mit neugeborenen Babys) an. Dieses Mütter-Coaching will ich bewerben. Die Flyer werden unter anderen an Ärzte und Hebammen weiter gegeben und dort in den Praxen ausliegen.
Aufgabenstellung
In meinem Logo herrschen die Farben orange und grau vor - es wäre schön, wenn sich diese Farben im Flyer wiederfinden würden - evtl. kombiniert mit mittelblau oder einem hellem grün.
Des weiteren möchte ich später Flyer im Din Lang Format (einseitig) mit anderen Angeboten erstellen. Das sollte mit dem Design dann auch möglich sein.
Der Schrifttyp soll bitte Arial sein, passend zum Logo. Ich habe bei Bildarko Fotos zu dem Thema erstanden, die ich stimmig finde. Diese Bilder sollten im Flyer genutzt werden.
Für diesen Flyer hätte ich gerne das Format: Falzblatt mit Wickelfalz - 279 x 219 mm

```html
<!DOCTYPE html>
<html lang="de">
<head>
<meta charset="utf-8">
<title>Flyer Coaching für Mütter – Karin Dossow</title>
<link href="https://fonts.googleapis.com/css2?family=Roboto:wght@300;400;500;700&family=Roboto+Condensed:wght@400;700&display=swap" rel="stylesheet">
<style>
  :root{
    --green:#7f8f3c;
    --orange:#eb9a30;
    --orange-text:#dd8c22;
    --brown:#8c4c14;
    --blue:#1a66a3;
    --ink:#474747;
    --soft:#6a6a6a;
    --paper:#ffffff;
    --paper-grey:#f2f2f1;
    --stage:#9dbfdd;
  }
  *{box-sizing:border-box;margin:0;padding:0}
  html,body{width:1200px;height:900px;overflow:hidden}
  body{
    background:var(--stage);
    font-family:"Roboto",Arial,sans-serif;
    color:var(--ink);
    position:relative;
  }
  .spread{
    position:absolute;top:243px;width:585px;height:413px;
    display:flex;box-shadow:0 2px 8px rgba(0,0,0,.18);
  }
  .spread--outer{left:10px}
  .spread--inner{left:605px}
  .panel{width:195px;height:100%;position:relative;display:flex;flex-direction:column;background:var(--paper)}
  .panel::after{content:"";position:absolute;left:0;right:0;bottom:0;height:7px;background:var(--accent)}
  .panel--green{--accent:var(--green)}
  .panel--orange{--accent:var(--orange)}
  .panel--blue{--accent:var(--blue)}

  /* headers with notch */
  .band{position:relative;height:98px;background:var(--accent);color:#fff;
    display:flex;flex-direction:column;align-items:center;justify-content:center;text-align:center;flex:none}
  .band::after{content:"";position:absolute;top:100%;left:var(--notch,50%);margin-left:-6px;
    border:6px solid transparent;border-top-color:var(--accent);border-bottom:0}
  .band--why{--notch:20%;font-weight:700;font-size:11.5px;line-height:16px;padding:0 10px}
  .band--why .claim{font-size:11px;line-height:13px;margin-top:3px}
  .band--quote{font-weight:700;font-size:13px;line-height:16.5px;position:relative}
  .quote-mark{position:absolute;font-family:Georgia,serif;font-size:20px;font-weight:700}
  .quote-mark--open{left:24px;top:25px}
  .quote-mark--close{right:30px;top:60px}

  .brand{font-size:16px;font-weight:400;color:var(--orange-text);letter-spacing:.2px}
  .brand--light{color:#fff}
  .brand-title{font-size:10px;font-weight:500;color:var(--soft);margin-top:7px}
  .brand-title--dark{color:var(--brown)}
  .brand-sub{font-size:9px;color:var(--ink);margin-top:2px}
  .brand-sub--dark{color:var(--brown)}

  .intro{padding:14px 8px 0;text-align:center}
  .body-copy{padding:14px 8px 0;font-size:6.8px;line-height:11px}
  .body-copy p+p{margin-top:11px}

  .contact{flex:1;text-align:center;font-size:6.8px;line-height:11px;padding-top:38px}
  .contact .name{font-size:9.5px;margin-bottom:1px}
  .contact p+p{margin-top:11px}
  .services{height:113px;background:var(--orange);text-align:center;color:#fff;position:relative;
    padding:16px 6px 0;font-size:6.8px;line-height:11px;margin-bottom:7px}
  .services::before{content:"";position:absolute;bottom:100%;left:50%;margin-left:-6px;
    border:6px solid transparent;border-bottom-color:var(--orange);border-top:0}
  .services h3{font-size:8.5px;font-weight:700;color:var(--brown);margin-bottom:2px}

  .photo{display:block;flex:none}
  .photo--mother{height:202px;background:linear-gradient(160deg,#5b4a47 0%,#c9a795 35%,#efe1d6 60%,#b8a8a8 100%)}
  .cover-brand{flex:1;display:flex;flex-direction:column;align-items:center;justify-content:center;text-align:center;padding-bottom:10px}

  /* inner spread */
  .spread--inner .panel{background:var(--paper-grey)}
  .spread--inner .panel--blue{background:var(--paper)}
  .top-rule{height:7px;background:var(--accent);position:relative;flex:none}
  .top-rule::after{content:"";position:absolute;top:100%;left:var(--notch,50%);margin-left:-6px;
    border:6px solid transparent;border-top-color:var(--accent);border-bottom:0}
  .section-head{font-family:"Roboto Condensed",Arial,sans-serif;font-size:9.5px;letter-spacing:.6px;
    color:var(--soft);margin-top:17px;text-transform:uppercase}
  .section-head span{color:var(--accent)}
  .situation{padding:0 8px;font-weight:300}
  .situation ul{list-style:none;margin-top:12px;font-size:6.6px;line-height:11px}
  .situation li{margin-bottom:11px}
  .situation li::before{content:"• ";color:var(--green)}
  .photo--tired{margin-top:auto;height:122px;margin-bottom:7px;
    background:linear-gradient(120deg,#e8e3dc 0%,#d6cfc7 40%,#8a8f9c 70%,#4f5b6f 100%)}

  .support{padding:0 8px;text-align:center;font-weight:300}
  .support .rule{width:22px;height:1px;background:var(--soft);margin:7px auto 0}
  .support h4{font-family:"Roboto Condensed",Arial,sans-serif;font-weight:400;font-size:8.5px;
    letter-spacing:.6px;color:var(--ink);margin:12px 0 5px}
  .support p{font-size:6.6px;line-height:11px}
  .support p+p{margin-top:11px}
  .support p.tight{margin-top:0}

  .way{padding:0 10px 0 16px;font-weight:300;font-size:6.6px;line-height:11px}
  .way .lead{margin-top:11px}
  .way h4{font-family:"Roboto Condensed",Arial,sans-serif;font-weight:700;font-size:8px;
    letter-spacing:.4px;color:var(--ink);margin:10px 0 8px}
  .offer{display:flex;align-items:center;gap:4px;font-size:8px;font-weight:500;color:var(--blue);margin:14px 0 5px}
  .offer svg{flex:none}
  .way p+p{margin-top:11px}
</style>
</head>
<body>

<!-- Außenseite -->
<section class="spread spread--outer" aria-label="Außenseite des Flyers">
  <article class="panel panel--green">
    <header class="band band--why">
      <div>Warum Coaching<br>extra für Mütter?</div>
      <div class="claim">Nur wer gut für sich selbst sorgt,<br>kann auch für andere da sein!</div>
    </header>
    <div class="intro">
      <div class="brand">Karin Dossow</div>
      <div class="brand-title">Coaching für Mütter</div>
      <div class="brand-sub">Begleitung - Stärkung - Beratung</div>
    </div>
    <div class="body-copy">
      <p>Als geprüfte psychologische Beraterin und Heilpraktikerin für Psychotherapie habe ich mich besonders auf das Coaching für Mütter spezialisiert.</p>
      <p>Hier setze ich die Methode des lösungsorientierten Kurzzeitcoachings ein, die den Fokus auf Stärken und Lösungen und nicht auf Probleme und Hindernisse legt.</p>
      <p>Das Konzept wird durch Achtsamkeits- und Entspannungsübungen abgerundet. Aspekte der „gewaltfreien“ = wertschätzenden Kommunikation werden für individuelle Konfliktlösungen im familiären Alltag genutzt.<br>Starten Sie mit einem neuen und liebevollen Blick auf Ihr Leben und auf Ihre Fähigkeiten.</p>
      <p>Sie werden erstaunt sein, was alles in Ihnen wohnt.</p>
    </div>
  </article>

  <article class="panel panel--orange">
    <header class="band">
      <div class="brand brand--light">Karin Dossow</div>
      <div class="brand-title brand-title--dark">Coaching für Mütter</div>
      <div class="brand-sub brand-sub--dark">Begleitung - Stärkung - Beratung</div>
    </header>
    <div class="contact">
      <p><span class="name">Karin Dossow</span><br>Heilpraktikerin für Psychotherapie<br>Geprüfte Psychologische Beraterin</p>
      <p>Telefon: 0160 555 12 340<br>Email: info@karin-dossow.de<br>www.karin-dossow.de</p>
      <p>Praxisgemeinschaft am Hain<br>Birkenweg 14<br>41460 Neuss am Rhein</p>
    </div>
    <div class="services">
      <h3>Weiteres Leistungsspektrum</h3>
      Psychologische Beratung<br>
      Stressbewältigung – Burnoutprävention<br>
      Achtsamkeitstraining – Palmtherapy<br>
      Lösungsfokussierte Kurzzeittherapie –<br>
      Gewaltfreie Kommunikation –<br>
      Energiearbeit – Geistiges Heilen – Reiki
    </div>
  </article>

  <article class="panel panel--blue">
    <header class="band band--quote">
      <span class="quote-mark quote-mark--open">”</span>
      <div>Das Baby ist da<br>und nichts ist mehr<br>wie es war</div>
      <span class="quote-mark quote-mark--close">“</span>
    </header>
    <div class="photo photo--mother" role="img" aria-label="Foto: junge Mutter hält ihr schlafendes Neugeborenes an der Schulter"></div>
    <div class="cover-brand">
      <div class="brand">Karin Dossow</div>
      <div class="brand-title">Coaching für Mütter</div>
      <div class="brand-sub">Begleitung - Stärkung - Beratung</div>
    </div>
  </article>
</section>

<!-- Innenseite -->
<section class="spread spread--inner" aria-label="Innenseite des Flyers">
  <article class="panel panel--green">
    <div class="top-rule" style="--notch:20%"></div>
    <div class="situation">
      <h2 class="section-head">Ihre <span>Situation</span></h2>
      <ul>
        <li>Haben Sie sich Ihr Mutterglück anders vorgestellt?<br>- Sie hatten sich so auf Ihr Baby gefreut, aber die Realität ist gar nicht so, wie Sie sie sich das gedacht haben?</li>
        <li>Fühlen Sie sich isoliert: plötzlich sind Sie allein in Ihrem Zuhause mit Ihrem Kind, Ihre Kollegen und Freunde führen weiterhin Ihr früheres Leben – Sie sind aber nicht mehr mit dabei?</li>
        <li>Das Verständnis Ihrer Umgebung für Ihre neue Situation fehlt. Sogar die Partnerschaft ist plötzlich ganz anders als sie es vorher war?</li>
        <li>Der Fokus aller richtet sich fast ausschließlich auf Ihr Kind - doch wo bleiben Sie eigentlich?</li>
        <li>Sie werden nur noch als Mutter wahrgenommen - kaum mehr als die Frau und die Persönlichkeit, die Sie vorher waren und auch immer noch sind?</li>
        <li>Sie fühlen sich oft erschöpft, ratlos, überfordert, unverstanden?</li>
      </ul>
    </div>
    <div class="photo photo--tired" role="img" aria-label="Foto: erschöpfte Mutter mit Baby im Arm neben einem Kinderbett"></div>
  </article>

  <article class="panel panel--orange">
    <div class="top-rule"></div>
    <div class="support">
      <h2 class="section-head">Meine <span>Unterstützung</span></h2>
      <div class="rule"></div>
      <h4>BEGLEITUNG</h4>
      <p>Die gute Nachricht: Sie müssen diese belastende Situation nicht allein bewältigen - erleben Sie Erleichterung, indem Sie sich von mir beraten lassen.</p>
      <p>Genießen SIE im Einzelcoaching, dass nur IHRE Situation zählt und SIE im Mittelpunkt stehen, denn als Coach gehe ich individuell auf Ihre Person und Situation ein.</p>
      <h4>STÄRKUNG</h4>
      <p>Verlagern Sie mit mir Ihren Fokus auf andere Sichtweisen und neue Wege. Entscheiden Sie sich für einen Weg, der zu Ihnen passt und Sie glücklich macht.</p>
      <p class="tight">Finden Sie die Mutterrolle, die es Ihnen ermöglicht gut für sich zu sorgen und bei sich zu bleiben und leben Sie so Ihre Bedürfnisse und Interessen im Einklang mit denen Ihrer Familie.</p>
      <h4>BERATUNG</h4>
      <p>Trotz Unmengen an Informationen fühlen sich viele Mütter mit ihren Themen alleine, hilflos und überfordert.</p>
      <p class="tight">Bei mir bleiben Sie nicht allein und ratlos: denn wir finden individuelle Antworten auf Ihre ganz persönlichen Fragen<br>Sie geben dabei die Themen und das Tempo an - ich begleite Sie aufmerksam, achtsam und wertschätzend!</p>
    </div>
  </article>

  <article class="panel panel--blue">
    <div class="top-rule" style="--notch:18%"></div>
    <div class="way">
      <h2 class="section-head">Unser <span>Weg</span></h2>
      <p class="lead">Gemeinsam können wir Ihre Situation durchleuchten.</p>
      <h4>MEIN ANGEBOT UMFASST...</h4>
      <div class="offer"><svg width="8" height="8" viewBox="0 0 8 8" aria-hidden="true"><circle cx="4" cy="4" r="4" fill="#474747"/><path d="M4 2v4M2 4h4" stroke="#fff" stroke-width="1.2"/></svg>Einzelcoaching</div>
      <p>Sie können wählen: das Coaching kann in meiner Praxis in Neuss oder gern auch bei Ihnen zu Hause stattfinden, so wie es gerade für Sie am besten passt.</p>
      <p>Die Zeit, die Sie und eventuell auch Ihr Partner sich für ein Coaching nehmen, ist überschaubar: maximal drei bis fünf Sitzungen à 60 Minuten können ausreichen, um Ihre momentane Situation anzuschauen und zu verändern.</p>
      <p>Wenn Einzelcoaching nicht das Richtige für Sie ist, können Sie sich auch für ein</p>
      <div class="offer"><svg width="8" height="8" viewBox="0 0 8 8" aria-hidden="true"><circle cx="4" cy="4" r="4" fill="#474747"/><path d="M4 2v4M2 4h4" stroke="#fff" stroke-width="1.2"/></svg>Gruppencoaching</div>
      <p>entscheiden. Lernen Sie dadurch Gleichgesinnte kennen und profitieren Sie in doppelter Hinsicht – nach dem Motto: „Lieber gemeinsam als einsam“.</p>
      <div class="offer"><svg width="8" height="8" viewBox="0 0 8 8" aria-hidden="true"><circle cx="4" cy="4" r="4" fill="#474747"/><path d="M4 2v4M2 4h4" stroke="#fff" stroke-width="1.2"/></svg>Telefoncoaching</div>
      <p>Sie bestimmen Ort und Zeit. Dieses Angebot könnte das Richtige für Sie sein, wenn Sie zeitlich oder örtlich gebunden sind.</p>
    </div>
  </article>
</section>

</body>
</html>
```